BRISKO FOOD: Window / Poster Advertising

Brisko is a store providing great, ready-to-eat, no-fuss food. Our main items are Pita meals, and Super Salads. And we have a need to advertise this food on the go business!

We have a large number of pedestrians passing the store three times per day, and require some advertising to promote or food, and attract these people. We are looking to have artwork created for use within the window and A-Frame. Effectively, a Poster Design. The size required is A1 (594mm x 841mm).

Common terms we use within the store and with our customers are:
- "Fine Food Take Out On The Go"
- "In and Out"
- "A Meal in a Pita"
These could be a source of promotion within the artwork

To keep a consistent branding, the "BRISKO" text/font, and Green Man image must be used (attached). Fonts: brisko font is called "goodmorningafternoon" and the font used for refood the multi-culti way is called "whipsmart" both of which can be downloaded for free. You can view our Facebook page here www.pallgrove.com/briskofood however, we are very open to the introduction of new colour and imagery. We are fond of the current Dunmore Mart advertising which has a slightly animated effect - example attached.

Hi all 

we have uploaded a few pictures which we would love you to draw some inspiration from. It is the design that is featured on most frostlop cups and frostlop machines in all Dunmore Marts. We really like this pop of colour and animated yet modernized look. We realised that although advertising the food is a great way to show the customer what we have we want a more generalised eye catching sort of advertisment that can be featured on our window no matter what the food we are serving. We are a very innovative shop that is constantly updating our menu and therefore we dont want one thing to be featured amongst the others. Please draw inspiration from the images uploaded aswell as from our facebook page (www.pallgrove.com/briskofood) to come up with something amazing!! were really loving the creativity and hope that these few images will help you understand exactly what we want. 

Warm Regards

```html
<!DOCTYPE html>
<html lang="en">
<head>
<meta charset="utf-8">
<title>Brisko Food – Window Poster</title>
<link rel="stylesheet" href="https://fonts.googleapis.com/css2?family=Comfortaa:wght@700&family=Rubik+Mono+One&family=Lilita+One&family=Fredoka:wght@700&family=Gochi+Hand&family=Amatic+SC:wght@700&display=swap">
<style>
  :root{
    --stage:#0d0d0f;
    --lavender:#8b82c1;
    --lavender-light:#b2aae0;
    --navy:#3a3a8c;
    --red:#e14a3c;
    --orange:#f3a23a;
    --cream:#fbe9cc;
    --plum:#4b2a5c;
    --magenta:#8c2c7c;
    --green:#7cc83a;
  }
  *{margin:0;padding:0;box-sizing:border-box}
  html,body{width:1200px;height:846px;overflow:hidden;background:var(--stage)}
  .poster-frame{position:absolute;left:300px;top:23px;width:601px;height:800px;overflow:hidden}
  .poster{position:absolute;left:0;top:0;width:533px;height:710px;transform:scale(1.1268);transform-origin:0 0;overflow:hidden;background:var(--lavender)}
  .poster-bg{position:absolute;inset:0}
  .abs{position:absolute}

  .tagline{left:153px;top:27px;font:700 15px/1 'Comfortaa',sans-serif;color:var(--cream);white-space:nowrap}
  .brand{left:158px;top:70px;display:flex;align-items:center;gap:12px}
  .brand-name{font:52px/1 'Rubik Mono One',sans-serif;color:var(--cream);letter-spacing:-2px}
  .brand-dot{width:44px;height:44px;border-radius:50%;background:var(--green)}

  .pun{font:31px/0.95 'Lilita One',sans-serif;color:var(--cream);text-transform:uppercase;text-shadow:2px 3px 0 var(--red);white-space:nowrap}
  .pun-chick{left:28px;top:60px;transform:rotate(4deg)}
  .pun-beef{left:32px;top:145px;transform:rotate(4deg)}

  .food-photo{left:223px;top:140px;width:165px;height:107px;border-radius:50% 50% 40% 40%;background:radial-gradient(ellipse at 50% 40%,#c23a6a 0%,#b4823e 55%,#7a4a22 100%)}

  .sign{left:333px;top:202px;width:200px;height:200px;border:9px solid var(--plum);border-radius:18px;background:var(--cream);transform:rotate(37deg)}
  .sign-text{left:356px;top:238px;width:170px;text-align:center;font:700 54px/0.92 'Fredoka',sans-serif;color:var(--plum);transform:rotate(-8deg);white-space:nowrap}

  .officer{left:0;top:272px;width:253px;height:438px;background:linear-gradient(180deg,#c3b4de 0%,#7d5d94 45%,#4b2a5c 100%);clip-path:polygon(62px 40px,90px 0,150px 0,175px 40px,175px 170px,253px 230px,253px 438px,0 438px,0 200px,62px 170px)}
  .badge-label{left:55px;top:455px;padding:4px 10px;background:var(--plum);color:var(--cream);font:700 24px/1 'Amatic SC',sans-serif;transform:rotate(-4deg);white-space:nowrap}

  .hand{font:19px/1.1 'Gochi Hand',cursive;color:var(--plum);white-space:nowrap}
  .hand .hi{color:var(--cream);font-size:27px;text-shadow:1px 1px 0 var(--orange)}
  .hand .hot{color:var(--orange)}
  .quip-sign{left:175px;top:276px;transform:rotate(-6deg)}
  .quip-check{left:198px;top:362px;transform:rotate(-6deg);line-height:1}

  .woman{left:423px;top:417px;width:110px;height:293px;border-radius:50% 50% 0 0 / 20% 20% 0 0;background:linear-gradient(180deg,#5a2f4e 0%,#e4b98c 40%,#cf9870 100%)}

  .slogan{left:238px;top:550px;font:700 56px/0.82 'Amatic SC',sans-serif;color:var(--cream);letter-spacing:1px;white-space:nowrap}
  .slogan .p{color:var(--magenta)}
  .slogan .d{color:var(--plum)}
</style>
</head>
<body>
<div class="poster-frame">
  <div class="poster">
    <svg class="poster-bg" width="533" height="710" viewBox="0 0 533 710" aria-hidden="true">
      <defs>
        <linearGradient id="warm" x1="0" y1="0" x2="0" y2="1">
          <stop offset="0" stop-color="#e14a3c"/>
          <stop offset="1" stop-color="#f3a23a"/>
        </linearGradient>
        <pattern id="stripes" width="10" height="10" patternUnits="userSpaceOnUse" patternTransform="rotate(45)">
          <rect width="4" height="10" fill="#ffffff" opacity=".08"/>
        </pattern>
      </defs>
      <rect width="533" height="710" fill="#8b82c1"/>
      <polygon points="150,0 330,0 300,710 260,710" fill="#b2aae0" opacity=".4"/>
      <rect width="533" height="710" fill="url(#stripes)"/>
      <polygon points="0,0 153,0 255,710 0,710" fill="url(#warm)"/>
      <polygon points="513,0 533,0 533,180 513,175" fill="#3a3a8c"/>
      <polygon points="203,167 240,140 240,157 330,157 330,180 240,180 240,195" fill="#fbe9cc" opacity=".65"/>
      <rect x="395" y="150" width="24" height="24" fill="#fbe9cc" opacity=".6"/>
      <rect x="428" y="150" width="24" height="24" fill="#fbe9cc" opacity=".6"/>
      <rect x="461" y="150" width="24" height="24" fill="#fbe9cc" opacity=".6"/>
      <polygon points="0,310 38,258 76,310 56,310 56,380 18,380 18,310" fill="#fbe9cc" opacity=".85"/>
      <polygon points="330,480 362,445 394,480 376,480 376,505 348,505 348,480" fill="#fbe9cc" opacity=".8"/>
      <polygon points="350,520 375,505 380,535" fill="#fbe9cc" opacity=".7"/>
    </svg>

    <p class="abs tagline">Refood the multi-culti way at</p>
    <div class="abs brand"><span class="brand-name">BRISKO</span><span class="brand-dot"></span></div>

    <p class="abs pun pun-chick">Chick<br>Magnet</p>
    <p class="abs pun pun-beef">Beef<br>Friends<br>Forever</p>

    <div class="abs food-photo" role="img" aria-label="Photo of a filled pita bread with meat, salad and sauce"></div>

    <div class="abs sign" aria-hidden="true"></div>
    <p class="abs sign-text">ready<br>-to-<br>eat</p>

    <div class="abs officer" role="img" aria-label="Illustration of a police officer in sunglasses with arms crossed"></div>
    <p class="abs badge-label">no-fuss food</p>

    <p class="abs hand quip-sign">DIDN'T<br>YOU <span class="hi">see</span><br>THAT <span class="hot">SIGN</span>?</p>
    <p class="abs hand quip-check">GO ON!<br><span class="hi">CHECK<br>IT!</span><br>IN A <span class="hot">PITA!</span></p>

    <div class="abs woman" role="img" aria-label="Illustration of a young woman with long dark hair"></div>

    <p class="abs slogan"><span class="p">F</span><span class="d">I</span><span class="p">NE</span> <span class="d">FOOD</span><br><span class="d">TAKE</span> <span class="p">OUT</span><br><span class="p">ON</span> THE GO!</p>
  </div>
</div>
</body>
</html>
```